"Tumbling Pebbles" Mobile 2D Game

We need a mobile design for the main screen of the game (with a popup design to select the ball color), for a Professional IT Team. Our initial game is "Tumbling Pebbles", classic board game for kids and even non kids. We would like to see design that suitable for mobile devices (small and tablet). The main concept of the game will be something similar to this video link: https://www.vidtrovex.com/watch?v=KqP7rLmwZtE

Please be sure the balls inside the game board have readable numbers. Thanks!

Requirements
Must have
• Separate layers for each UI component so it can be exported easily

```html
<!DOCTYPE html>
<html lang="en">
<head>
<meta charset="utf-8">
<title>Tumbling Pebbles – Game Board</title>
<link rel="stylesheet" href="https://fonts.googleapis.com/css2?family=Bebas+Neue&display=swap">
<style>
  :root {
    --screen-bg: #f2f2f2;
    --grid-line: #6e5325;
    --block: #6b4f24;
    --ink: #6b4a16;
    --btn-top: #fbdc4c;
    --btn-bottom: #f2a519;
    --btn-edge: #c98a0f;
    --btn-shadow: #a8a8a8;
    --green-top: #5ee86a;
    --green-bottom: #3cbf2e;
    --green-edge: #2c8d24;
    --orange-top: #ffb43a;
    --orange-bottom: #f5503a;
    --orange-edge: #c2621d;
    --white: #ffffff;
  }
  * { box-sizing: border-box; margin: 0; padding: 0; }
  html, body { width: 1200px; height: 852px; overflow: hidden; }
  body {
    background: var(--screen-bg);
    font-family: "Bebas Neue", "Oswald", sans-serif;
    position: relative;
    color: var(--ink);
  }
  .game-screen { position: absolute; left: 0; top: 150px; width: 1200px; height: 552px; }

  .pill-button {
    position: absolute;
    display: flex; align-items: center; justify-content: center;
    border-radius: 999px;
    background: linear-gradient(180deg, var(--btn-top) 0%, var(--btn-bottom) 100%);
    border: 2px solid var(--btn-edge);
    box-shadow: 0 5px 0 var(--btn-shadow);
    color: var(--ink);
    letter-spacing: 0.5px;
  }
  .help-button { left: 39px; top: 19px; width: 76px; height: 46px; font-size: 34px; }
  .score-button { left: 1096px; top: 19px; width: 76px; height: 46px; font-size: 23px; }
  .back-button { left: 33px; top: 462px; width: 162px; height: 66px; font-size: 46px; }
  .options-button { left: 1016px; top: 462px; width: 162px; height: 66px; font-size: 42px; }

  .score-badge {
    position: absolute;
    width: 92px; height: 92px;
    border-radius: 50%;
    display: flex; align-items: center; justify-content: center;
    color: var(--white);
    font-size: 46px;
    box-shadow: 0 5px 0 var(--btn-shadow);
    text-shadow: 0 2px 0 rgba(0,0,0,0.25);
  }
  .player-total { left: 166px; top: 224px; background: linear-gradient(180deg, var(--green-top), var(--green-bottom)); border: 3px solid var(--green-edge); }
  .opponent-total { left: 978px; top: 224px; background: linear-gradient(180deg, var(--orange-top), var(--orange-bottom)); border: 3px solid var(--orange-edge); }

  .game-board { position: absolute; left: 349px; top: 69px; width: 512px; height: 410px; }
  .board-label { font-family: "Bebas Neue", "Oswald", sans-serif; fill: var(--ink); }
  .ball-label { font-family: "Bebas Neue", "Oswald", sans-serif; fill: var(--white); }
</style>
</head>
<body>
<main class="game-screen">
  <div class="pill-button help-button">?</div>
  <div class="pill-button score-button">SCORE</div>

  <div class="score-badge player-total">600</div>
  <div class="score-badge opponent-total">130</div>

  <svg class="game-board" viewBox="0 0 512 410" xmlns="http://www.w3.org/2000/svg">
    <defs>
      <linearGradient id="orangeBall" x1="0" y1="0" x2="0" y2="1">
        <stop offset="0" stop-color="#ffb43a"/><stop offset="1" stop-color="#f5503a"/>
      </linearGradient>
      <linearGradient id="greenBall" x1="0" y1="0" x2="0" y2="1">
        <stop offset="0" stop-color="#5ee86a"/><stop offset="1" stop-color="#3cbf2e"/>
      </linearGradient>
      <linearGradient id="arrowTile" x1="0" y1="0" x2="0" y2="1">
        <stop offset="0" stop-color="#fbdc4c"/><stop offset="1" stop-color="#f2a519"/>
      </linearGradient>
      <g id="top-ball"><circle r="18" fill="url(#orangeBall)" stroke="#9a4a16" stroke-width="1.5"/></g>
      <path id="arrow-right" d="M-14,-5 H2 V-13 L15,0 L2,13 V5 H-14 Z" fill="#6b4a16"/>
    </defs>

    <!-- blocked cells -->
    <rect class="block-cell" x="307.2" y="51.25" width="51.2" height="51.25" fill="#6b4f24"/>
    <rect class="block-cell" x="51.2" y="153.75" width="51.2" height="51.25" fill="#6b4f24"/>
    <rect class="block-cell" x="307.2" y="307.5" width="51.2" height="51.25" fill="#6b4f24"/>

    <!-- arrow tiles -->
    <g class="arrow-tile">
      <rect x="153.6" y="102.5" width="51.2" height="51.25" fill="url(#arrowTile)"/>
      <use href="#arrow-right" transform="translate(179.2 128.1)"/>
    </g>
    <g class="arrow-tile">
      <rect x="307.2" y="153.75" width="51.2" height="51.25" fill="url(#arrowTile)"/>
      <use href="#arrow-right" transform="translate(332.8 179.4) scale(-1 1)"/>
    </g>
    <g class="arrow-tile">
      <rect x="51.2" y="307.5" width="51.2" height="51.25" fill="url(#arrowTile)"/>
      <use href="#arrow-right" transform="translate(76.8 333.1) scale(-1 1)"/>
    </g>

    <!-- grid lines -->
    <g stroke="#6e5325" stroke-width="1.6" fill="none">
      <rect x="0.8" y="0.8" width="510.4" height="408.4"/>
      <path d="M51.2 0V410M102.4 0V410M153.6 0V410M204.8 0V410M256 0V410M307.2 0V410M358.4 0V410M409.6 0V410M460.8 0V410"/>
      <path d="M0 51.25H512M0 102.5H512M0 153.75H512M0 205H512M0 256.25H512M0 307.5H512M0 358.75H512"/>
    </g>

    <!-- starting balls -->
    <g class="start-row">
      <use href="#top-ball" x="25.6" y="25.6"/><use href="#top-ball" x="76.8" y="25.6"/>
      <use href="#top-ball" x="128" y="25.6"/><use href="#top-ball" x="179.2" y="25.6"/>
      <use href="#top-ball" x="230.4" y="25.6"/><use href="#top-ball" x="281.6" y="25.6"/>
      <use href="#top-ball" x="332.8" y="25.6"/><use href="#top-ball" x="384" y="25.6"/>
      <use href="#top-ball" x="435.2" y="25.6"/><use href="#top-ball" x="486.4" y="25.6"/>
    </g>

    <!-- board balls -->
    <g class="board-ball">
      <circle cx="128" cy="128.1" r="18" fill="url(#greenBall)" stroke="#2c6d1e" stroke-width="1.5"/>
      <text class="ball-label" x="128" y="136" text-anchor="middle" font-size="22">10</text>
    </g>
    <g class="board-ball">
      <circle cx="486.4" cy="128.1" r="18" fill="url(#orangeBall)" stroke="#9a4a16" stroke-width="1.5"/>
      <text class="ball-label" x="486.4" y="136" text-anchor="middle" font-size="22">20</text>
    </g>
    <g class="board-ball">
      <circle cx="384" cy="179.4" r="18" fill="url(#greenBall)" stroke="#2c6d1e" stroke-width="1.5"/>
      <text class="ball-label" x="384" y="187.3" text-anchor="middle" font-size="22">10</text>
    </g>
    <g class="board-ball">
      <circle cx="230.4" cy="230.6" r="18" fill="url(#orangeBall)" stroke="#9a4a16" stroke-width="1.5"/>
      <text class="ball-label" x="230.4" y="238.5" text-anchor="middle" font-size="22">20</text>
    </g>

    <!-- cell points -->
    <text class="board-label" x="9" y="243" font-size="32">10</text>
    <text class="board-label" x="367" y="294" font-size="32">20</text>
  </svg>

  <div class="pill-button back-button">BACK</div>
  <div class="pill-button options-button">OPTIONS</div>
</main>
</body>
</html>
```